Halvey’s

I would like a high class looking card with my logo and contact details (as per uploaded) Elegant, professional and highest quality feel

The following text included …..
“All commercial and residential painting work, large or small. Highest quality finishes and service.”

Industry/Entity Type

Painting

Contact Information for Business Card

Name, phone number, address, email address, company logo

Requirements
Must have
• Double sided

```html
<!DOCTYPE html>
<html lang="en">
<head>
<meta charset="utf-8">
<title>Halvey’s – Business Card</title>
<link href="https://fonts.googleapis.com/css2?family=Montserrat:wght@700&family=Open+Sans:wght@400;600&display=swap" rel="stylesheet">
<style>
  :root {
    --backdrop: #222223;
    --card: #2a2a2b;
    --card-deep: #232324;
    --card-panel: #2d2d2e;
    --gold: #b98a4a;
    --silver: #c9c9cb;
    --white: #f2f2f2;
    --shadow: rgba(0,0,0,0.55);
  }
  * { box-sizing: border-box; margin: 0; padding: 0; }
  html, body { width: 1200px; height: 780px; overflow: hidden; background: var(--backdrop); }
  .canvas {
    position: relative; width: 1200px; height: 780px;
    display: flex; justify-content: center; align-items: center; gap: 44px;
  }
  .card {
    position: relative; width: 330px; height: 560px; border-radius: 28px;
    background: var(--card); overflow: hidden;
    box-shadow: 0 18px 40px var(--shadow);
  }
  /* Front */
  .card--front {
    background: radial-gradient(ellipse at 40% 50%, #323233 0%, var(--card) 55%, var(--card-deep) 100%);
  }
  .front-brand {
    position: absolute; left: 50%; top: 50%;
    transform: translate(-50%, -50%) rotate(-90deg);
    display: flex; align-items: center; gap: 18px; white-space: nowrap;
  }
  .front-brand__name {
    font-family: "Open Sans", sans-serif; font-weight: 400;
    font-size: 50px; letter-spacing: 4px; color: var(--silver);
  }
  .front-brand__dot {
    width: 64px; height: 64px; border-radius: 50%;
    border: 2px solid var(--silver);
  }
  /* Back */
  .back-layers { position: absolute; inset: 0; }
  .back-brand {
    position: absolute; top: 46px; left: 0; right: 0;
    display: flex; justify-content: center; align-items: center; gap: 10px;
  }
  .back-brand__name {
    font-family: "Open Sans", sans-serif; font-weight: 400;
    font-size: 30px; letter-spacing: 2px; color: var(--gold);
  }
  .back-brand__dot { width: 34px; height: 34px; border-radius: 50%; border: 2px solid var(--gold); }
  .contact {
    position: absolute; top: 150px; left: 0; right: 0; text-align: center;
    font-family: "Open Sans", sans-serif; color: var(--white);
  }
  .contact__name {
    font-family: "Montserrat", sans-serif; font-weight: 700;
    font-size: 25px; color: var(--gold); line-height: 1.1;
  }
  .contact__role { font-size: 13px; font-weight: 600; margin-top: 2px; }
  .contact__icons { display: flex; justify-content: center; gap: 8px; margin: 12px 0 8px; }
  .icon {
    width: 22px; height: 22px; border-radius: 50%; background: var(--gold);
    display: flex; align-items: center; justify-content: center;
  }
  .icon svg { width: 12px; height: 12px; }
  .contact__line { font-size: 13.5px; line-height: 1.35; }
  .contact__pin { margin: 10px auto 6px; }
  .tagline {
    position: absolute; bottom: 36px; left: 0; right: 0; text-align: center;
    font-family: "Open Sans", sans-serif; font-size: 12.5px; line-height: 1.45; color: var(--white);
  }
</style>
</head>
<body>
<main class="canvas">

  <section class="card card--front" aria-label="Card front">
    <div class="front-brand">
      <span class="front-brand__dot"></span>
      <span class="front-brand__name">HALVEY’S</span>
    </div>
  </section>

  <section class="card card--back" aria-label="Card back">
    <svg class="back-layers" viewBox="0 0 330 560" preserveAspectRatio="none" aria-hidden="true">
      <defs>
        <filter id="panel-shadow" x="-20%" y="-20%" width="140%" height="160%">
          <feDropShadow dx="0" dy="6" stdDeviation="7" flood-color="#000" flood-opacity="0.55"/>
        </filter>
      </defs>
      <rect width="330" height="560" fill="var(--card-deep)"/>
      <path d="M0 0 H330 V330 C300 400 240 440 150 455 C90 462 40 440 0 420 Z" fill="#282829" filter="url(#panel-shadow)"/>
      <path d="M0 0 H330 V200 C330 330 260 410 150 420 C90 425 40 410 0 395 Z" fill="var(--card-panel)" filter="url(#panel-shadow)"/>
    </svg>

    <div class="back-brand">
      <span class="back-brand__name">HALVEY’S</span>
      <span class="back-brand__dot"></span>
    </div>

    <div class="contact">
      <p class="contact__name">Daniel Halvey</p>
      <p class="contact__role">Owner</p>
      <div class="contact__icons">
        <span class="icon"><svg viewBox="0 0 24 24"><path fill="#fff" d="M6.6 10.8a15 15 0 0 0 6.6 6.6l2.2-2.2c.3-.3.7-.4 1-.2 1.1.4 2.3.6 3.6.6.6 0 1 .4 1 1V20c0 .6-.4 1-1 1A17 17 0 0 1 3 4c0-.6.4-1 1-1h3.5c.6 0 1 .4 1 1 0 1.3.2 2.5.6 3.6.1.3 0 .7-.2 1z"/></svg></span>
        <span class="icon"><svg viewBox="0 0 24 24"><path fill="#fff" d="M3 5h18v14H3z"/><path d="M3 5l9 7 9-7" fill="none" stroke="#b98a4a" stroke-width="2"/></svg></span>
        <span class="icon"><svg viewBox="0 0 24 24"><circle cx="12" cy="12" r="9" fill="none" stroke="#fff" stroke-width="2"/><path d="M3 12h18M12 3c3 3 3 15 0 18M12 3c-3 3-3 15 0 18" fill="none" stroke="#fff" stroke-width="1.6"/></svg></span>
      </div>
      <p class="contact__line">021 555 0142</p>
      <p class="contact__line">www.halveys.example</p>
      <p class="contact__line">daniel@halveys.example</p>
      <div class="icon contact__pin"><svg viewBox="0 0 24 24"><path fill="#fff" d="M12 2a7 7 0 0 0-7 7c0 5 7 13 7 13s7-8 7-13a7 7 0 0 0-7-7zm0 9.5A2.5 2.5 0 1 1 12 6.5a2.5 2.5 0 0 1 0 5z"/></svg></div>
      <p class="contact__line">42 Kowhai Lane,</p>
      <p class="contact__line">Riverton, 3150</p>
    </div>

    <p class="tagline">All commercial and residential<br>painting work, large or small.<br>Highest quality finishes and service.</p>
  </section>

</main>
</body>
</html>
```